依頼詳細
・アルミパウチパッケージの300mlタイプ。シンプルでありながら、女性の可愛らしさとオシャレ感漂うデザイン希望。ビーチ味なので、色はピンク系が希望だが、ピンク×白(マット系)が映えるのではないかと思われますが、使用する色の割合によってイメージが変わると思います。センスあれば色は気にせず自由にデザインください。
・何色使用するかですが、シンプルに2色~3色が良いかと思います。
・サイズに関しては、縦165mm×横84mm(折り目部分や貼付け部分を別途ファイル添付)

記載項目
サイズ縦165mm×横84mm。パッケージ素材はアルミパウチ、表面は「TANQEP」のネーミング文字、「賞味期限」は指定位置に入れてください。
※詳細は、添付ファイルをご参照ください。
希望イメージ
• +5 0 +5
• シンプル
複雑
• 単色
カラフル
• 暗い
明るい
• 日常
高級
• 遊び心
厳粛
• 未来的
伝統的
• 女性的
男性的
希望する色
赤系
納品ファイル
• イラストレーター形式 (.ai)
依頼公開後の追記内容
報酬金額をアップし、より多くのご提案をいただきたく、要望に合ったデザインを期待しております。ランサーの方々、何卒よろしくお願いいたします。
報酬金額をアップ致しましたので、より多くのご提案をいただき、要望に適ったデザインが、ランサーの方々より送られてくることを期待しております。何卒、宜しくお願いいたします。
ランサーの方々より延長依頼のご要望がございましたのと、もう少しデザイン提案が欲しいので延長させていただきました。
かなりクオリティの高いデザインを数多くご提案いただき検討致しましたが、「これだ!」という「インパクトある№1デザイン」がないため、2日間延長させていただきます。シャンプーに見えてしまうデザインが多い気がします。
【ヒアルロン酸、コラーゲン等の美容飲料】のイメージを再度ご考慮いただければ幸いです!!
デザイン決定後、弊社は12/29~1/6まで年末年始休業のため、年始の1/7以降に細部等のご相談をさせていただきたいと存じます。裏面の文面等もご相談させていただく予定ですので、何卒宜しくお願いいたします。
ランサーの皆様、数多くのご提案を賜り心より感謝申し上げます。想定以上の際立った素晴らしいデザインがあり、大変嬉しく存じます。弊社は年末年始の休業期間となり、やり取りが出来なくなりますため最大延長(1/6日まで)をさせていただきます。
年始は1/7(月)より、新たにやり取りをさせていただきたく存じます。
その際は、ご対応の程 何卒よろしくお願いいたします。
それでは皆様、良いお年をお迎えください。
感謝
■ 選んだ理由

デザインが、気品と可愛さもあり、素敵な女性がこの商品を手にしているイメージが湧き、女性社員からも多くの賛同をいただいたため最終的にこのデザインに決定させていただきました。また、ぷるるん感も可愛く表現され、色使いもきれいなピンクで、成分表示もわかり易くて、高級感も漂いニーズに合致したものだったので、選定させていただきました。
また、こちらのランサー様は、度重なる細部の修正にも的確且つ迅速にご対応いただきましたことに心より御礼申し上げます。本当に、ありがとうございました。

■ 提案者全員のお礼・コメント

全80提案で、多くのランサーの方々よりデザインをいただき心より感謝しております。今回は、採用されなかったランサーの皆様、真摯なご対応ありがとうございました。また別の機会の際は、何卒よろしくお願いいたします。御礼まで。

```html
<!DOCTYPE html>
<html lang="ja">
<head>
<meta charset="utf-8">
<title>TANQEP パウチパッケージ</title>
<link rel="stylesheet" href="https://fonts.googleapis.com/css2?family=Cormorant+Garamond:wght@400&family=Noto+Sans+JP:wght@400;500&display=swap">
<style>
  :root {
    --pink: #e5538f;
    --coral: #ee7a5c;
    --peach-soft: #f7a8b8;
    --ink: #7a7a7a;
    --pouch: #ffffff;
    --edge: #d9d9d9;
    --bg: #ffffff;
  }
  html, body {
    margin: 0;
    padding: 0;
    width: 850px;
    height: 1200px;
    overflow: hidden;
    background: var(--bg);
  }
  .canvas {
    position: relative;
    width: 850px;
    height: 1200px;
    font-family: "Noto Sans JP", sans-serif;
    color: var(--ink);
  }
  .swatch {
    position: absolute;
    top: 16px;
    width: 70px;
    height: 52px;
  }
  .swatch-pink { left: 40px; background: var(--pink); }
  .swatch-coral { left: 150px; background: var(--coral); }
  .swatch-label {
    position: absolute;
    top: 74px;
    width: 70px;
    font-size: 14px;
    text-align: center;
    color: #555;
  }
  .swatch-label.pink { left: 40px; }
  .swatch-label.coral { left: 150px; }

  .spout {
    position: absolute;
    left: 380px;
    top: 60px;
    width: 90px;
    height: 84px;
    background: linear-gradient(90deg, #e6e6e6, #fafafa 50%, #e2e2e2);
    border: 1px solid var(--edge);
    border-radius: 6px 6px 2px 2px;
  }
  .pouch {
    position: absolute;
    left: 170px;
    top: 142px;
    width: 510px;
    height: 1030px;
    background: var(--pouch);
    border: 2px solid var(--edge);
    border-radius: 18px 18px 28px 28px;
    box-sizing: border-box;
  }
  .claim-label {
    position: absolute;
    left: 58px;
    top: 44px;
    font-size: 14px;
    color: var(--ink);
    letter-spacing: 0.05em;
  }
  .category {
    position: absolute;
    top: 84px;
    width: 100%;
    text-align: center;
    font-size: 17px;
    color: var(--ink);
    letter-spacing: 0.08em;
  }
  .brand {
    position: absolute;
    top: 112px;
    width: 100%;
    text-align: center;
    font-family: "Cormorant Garamond", serif;
    font-weight: 400;
    font-size: 84px;
    line-height: 1;
    letter-spacing: 0.16em;
    color: var(--ink);
    text-indent: 0.16em;
  }
  .brand-reading {
    position: absolute;
    top: 194px;
    width: 100%;
    text-align: center;
    font-size: 14px;
    letter-spacing: 0.2em;
    color: var(--ink);
  }
  .ingredient-cycle {
    position: absolute;
    left: 95px;
    top: 220px;
    width: 320px;
    height: 320px;
  }
  .cycle-label {
    font-family: "Noto Sans JP", sans-serif;
    font-size: 15px;
    font-weight: 500;
    fill: #ffffff;
  }
  .flavor {
    font-family: "Noto Sans JP", sans-serif;
    font-size: 15px;
    font-weight: 500;
    fill: var(--pink);
  }
  .volume {
    position: absolute;
    top: 560px;
    width: 100%;
    text-align: center;
    font-size: 22px;
    color: var(--ink);
    letter-spacing: 0.04em;
  }
  .diet-note {
    position: absolute;
    top: 626px;
    width: 100%;
    text-align: center;
    font-size: 12.5px;
    color: var(--pink);
    letter-spacing: 0.03em;
  }
</style>
</head>
<body>
<div class="canvas">
  <div class="swatch swatch-pink"></div>
  <div class="swatch swatch-coral"></div>
  <div class="swatch-label pink">DIC 75</div>
  <div class="swatch-label coral">DIC 81</div>

  <div class="spout"></div>
  <div class="pouch">
    <div class="claim-label">機能性表示食品</div>
    <div class="category">ヒアルロン酸入り美容飲料</div>
    <div class="brand">TANQEP</div>
    <div class="brand-reading">タンケプ</div>

    <svg class="ingredient-cycle" viewBox="0 0 320 320" aria-label="配合成分のサイクル図">
      <defs>
        <radialGradient id="peachTone" cx="45%" cy="40%" r="60%">
          <stop offset="0" stop-color="#fbd0d6"/>
          <stop offset="1" stop-color="var(--peach-soft)"/>
        </radialGradient>
      </defs>
      <g fill="none" stroke="var(--pink)" stroke-width="30">
        <path d="M 172 41 A 120 120 0 0 1 268 106"/>
        <path d="M 276 128 A 120 120 0 0 1 262 218"/>
        <path d="M 248 238 A 120 120 0 0 1 108 268"/>
        <path d="M 88 256 A 120 120 0 0 1 40 168"/>
        <path d="M 42 140 A 120 120 0 0 1 146 41"/>
      </g>
      <g fill="var(--pink)">
        <polygon points="262,92 290,110 256,122"/>
        <polygon points="284,204 262,234 252,206"/>
        <polygon points="100,282 80,248 112,252"/>
        <polygon points="24,172 42,142 56,170"/>
        <polygon points="150,20 172,42 146,60"/>
      </g>
      <text class="cycle-label" x="208" y="60" text-anchor="middle" transform="rotate(22 208 60)">コラーゲン</text>
      <text class="cycle-label" x="276" y="172" text-anchor="middle" transform="rotate(90 276 172)">ビタミンC</text>
      <text class="cycle-label" x="180" y="286" text-anchor="middle" transform="rotate(-15 180 286)">大豆</text>
      <text class="cycle-label" x="52" y="214" text-anchor="middle" transform="rotate(-62 52 214)">乳酸菌</text>
      <text class="cycle-label" x="84" y="84" text-anchor="middle" transform="rotate(-45 84 84)">セラミド</text>
      <circle cx="160" cy="150" r="46" fill="url(#peachTone)" role="img" aria-label="桃のイラスト"/>
      <rect x="118" y="206" width="84" height="26" rx="4" fill="#ffffff"/>
      <text class="flavor" x="160" y="225" text-anchor="middle">ピーチ味</text>
    </svg>

    <div class="volume">300ml</div>
    <div class="diet-note">食生活は、主食、主菜、副菜を基本に、食事のバランスを。</div>
  </div>
</div>
</body>
</html>
```